Website redesign: OLU - Bright Reel Studio

Web Design Brief
I'm looking for a redesign of our website https://www.brightreel.studio/. The website is built with Wix.

We are an AI Video Production Agency named OLU that uses AI-technology to create videos for our clients. We use the platform vormetric.io to generate videos.

Use case:
A financial services company is looking for a way to transform their inhouse training content to video.
They visit brightreel.studio and submit a brief.
Several production packages are presented, and the company selects the one that suits them best. Pricing is agreed upon, and the company provides the necessary scripts and documentation.

As a growing agency, our web page's primary objective is to acquire business leads (companies seeking professional video services) and to communicate our unique AI-driven approach to video production. The landing page will include a form for potential clients to fill out their requirements, as well as a showcase of our AI's capabilities in video production.

We have not yet chosen a color palette, but we are looking for a design that will inspire confidence in our clients while also highlighting the innovative and creative nature of our service. The overall theme should be sleek, modern, and visual, as our core offering is video creation and editing.

Current website:
https://www.brightreel.studio/

Competitors:
https://www.clipforge.pro/
https://pixelbound.ai/
https://www.quillspots.com/vormetric

Inspiration:
https://www.vormetric.io/
https://lumo.co.uk/
https://crispnorth.co/
https://www.bluefennel.com/

Target Market(s)

Director's of training and others who work with video at companies with $10M+ in revenue and 100+ employees.

Industry/Entity Type

Video Services Agency

Coding

Coded - Design and coding required

Number of Pages Required

1 page

Font styles to use
Sans Serif

Requirements
Must have
• Clear CTA and services showcase above the fold. Include "Services" and "Blog" section.
Nice to have
• Reviews / Proof of concept

```html
<!DOCTYPE html>
<html lang="en">
<head>
<meta charset="utf-8">
<title>OLU - Bright Reel Studio — Landing Page Variants</title>
<link href="https://fonts.googleapis.com/css2?family=Lexend:wght@400;500;600&family=Roboto:wght@400;500&display=swap" rel="stylesheet">
<style>
:root{
  --board:#333333;
  --white:#ffffff;
  --ink:#1b1f26;
  --muted:#5b6270;
  --soft:#f1f1f1;
  --band:#ececec;
  --star:#f5b400;
}
.theme-blue{
  --hero-a:#1f86f4; --hero-b:#0c56e2;
  --accent:#1565e8; --accent-2:#2a9ff0;
  --icon-a:#2aa3ee; --icon-b:#0d5cd4;
  --cta:#1fb8f0;
}
.theme-night{
  --hero-a:#12253b; --hero-b:#06101d;
  --accent:#4fc3c8; --accent-2:#4fc3c8;
  --icon-a:#0f1e30; --icon-b:#0a1522;
  --cta:#4fc3c8;
}
*{margin:0;padding:0;box-sizing:border-box}
html,body{width:918px;height:1200px;overflow:hidden;background:var(--board)}
body{position:relative;font-family:"Roboto",sans-serif;color:var(--ink)}
h1,h2,h3,h4{font-weight:400}
.page{position:absolute;top:52px;width:375px;height:1094px;background:var(--white);overflow:hidden}
.page.left{left:59px}
.page.right{left:481px}
.page > *{position:absolute}

/* header / hero */
.hero{left:0;top:0;width:375px;height:200px;background:radial-gradient(circle at 70% 90%,rgba(255,255,255,.12),transparent 55%),linear-gradient(135deg,var(--hero-a),var(--hero-b))}
.logo{left:33px;top:8px;display:flex;align-items:center;gap:4px;color:var(--white)}
.logo-dot{width:18px;height:18px;border:2px solid currentColor;border-radius:50%}
.logo-name{font-family:"Lexend",sans-serif;font-weight:500;font-size:17px;letter-spacing:1px;line-height:1}
.logo-tag{position:absolute;left:22px;top:19px;font-family:"Lexend",sans-serif;font-size:2.6px;letter-spacing:.8px;white-space:nowrap}
.nav{top:14px;left:179px;font-family:"Lexend",sans-serif;font-size:4.6px;color:var(--white)}
.nav span{position:absolute;white-space:nowrap}
.btn-contact{left:290px;top:8px;width:49px;height:14px;border-radius:7px;background:var(--cta);color:var(--white);font-family:"Lexend",sans-serif;font-size:4.6px;letter-spacing:.3px;display:flex;align-items:center;justify-content:center}
.hero-title{left:33px;top:58px;width:170px;font-family:"Lexend",sans-serif;font-weight:400;font-size:10px;line-height:17px;letter-spacing:.5px;color:var(--white);white-space:nowrap}
.hero-points{left:35px;top:134px;list-style:none;font-family:"Lexend",sans-serif;font-size:5.4px;letter-spacing:.3px;color:var(--white)}
.hero-points li{display:flex;align-items:center;gap:3px;height:11.5px}
.hero-points li::before{content:"";width:5px;height:5px;border-radius:50%;border:1px solid rgba(255,255,255,.8)}
.video{left:207px;top:61px;width:133px;height:107px;border:2px solid var(--white);border-radius:5px;background:linear-gradient(90deg,#d9dde0,#f3f4f4 40%,#3a2c27 60%,#c9cfd2)}
.play{left:266px;top:107px;width:16px;height:16px;border-radius:50%;background:var(--cta);display:flex;align-items:center;justify-content:center}

/* section titles */
.sec-title{left:0;width:375px;text-align:center;font-family:"Lexend",sans-serif;font-weight:400;font-size:11.5px;letter-spacing:.8px;color:var(--ink)}

/* services */
.svc-card{left:140px;top:258px;width:92px;height:99px;background:var(--white);border-radius:3px;box-shadow:0 2px 10px rgba(0,0,0,.09)}
.svc{width:96px;text-align:center}
.svc-icon{width:24px;height:24px;margin:0 auto;border-radius:50%;background:linear-gradient(160deg,var(--icon-a),var(--icon-b));display:flex;align-items:center;justify-content:center}
.svc-title{margin-top:10px;font-family:"Lexend",sans-serif;font-size:5.6px;letter-spacing:.4px;line-height:8.5px;color:var(--ink)}
.svc-text{margin-top:3px;font-size:4.3px;line-height:8px;color:var(--muted)}

/* about */
.about-band{left:0;top:482px;width:375px;height:142px;background:var(--band)}
.about-bar{left:37px;top:512px;width:2px;height:24px;background:linear-gradient(var(--accent) 45%,#9a9a9a 45%)}
.about-title{left:46px;top:511px;font-family:"Lexend",sans-serif;font-size:10.5px;letter-spacing:.7px}
.about-text{left:46px;top:529px;width:148px;font-size:4.5px;line-height:8px;color:var(--muted)}
.btn-pill{border-radius:8px;background:var(--accent);color:var(--white);font-family:"Lexend",sans-serif;font-size:4.5px;display:flex;align-items:center;justify-content:center}
.btn-learn{left:44px;top:582px;width:49px;height:16px}
.about-visual{left:216px;top:497px;width:112px;height:112px;border-radius:50%;background:radial-gradient(circle,#e9ecef 40%,#b9c0c6 60%,var(--accent) 62%,var(--icon-b) 100%)}

/* testimonials */
.review{background:var(--white);border-radius:3px;box-shadow:0 2px 10px rgba(0,0,0,.08);overflow:hidden}
.review.side{background:var(--soft);box-shadow:none}
.rv-avatar{position:absolute;left:7px;top:6px;width:15px;height:15px;border-radius:50%;background:linear-gradient(#c99a7a,#6b4a3a)}
.rv-name{position:absolute;left:29px;top:7px;font-family:"Lexend",sans-serif;font-size:5.6px;letter-spacing:.3px;white-space:nowrap}
.rv-sub{position:absolute;left:29px;top:15px;font-size:3.4px;color:#9aa0a8}
.rv-text{position:absolute;left:30px;top:22px;width:140px;font-size:3.8px;line-height:8px;color:var(--muted)}
.rv-meta{position:absolute;left:30px;top:60px;display:flex;align-items:center;gap:3px;font-size:3.2px;color:var(--accent)}
.stars{color:var(--star);font-size:4.6px;letter-spacing:.6px}
.track{left:116px;top:774px;width:140px;height:1px;background:#e3e3e3}
.track-active{left:174px;top:773px;width:28px;height:2px;background:var(--accent)}

/* blog */
.post{width:127px;height:100px;overflow:visible}
.post-photo{position:absolute;inset:0;background:linear-gradient(180deg,#c8ccd0 0%,#8d949a 45%,#3c4147 100%)}
.post-title{position:absolute;left:7px;top:60px;font-family:"Lexend",sans-serif;font-weight:400;font-size:7.4px;letter-spacing:.5px;color:var(--white);white-space:nowrap}
.post-text{position:absolute;left:7px;top:73px;width:118px;font-size:4.4px;line-height:8px;color:#e9ecef}
.post-go{position:absolute;left:104px;top:92px;width:16px;height:16px;border-radius:50%;background:var(--accent);border:1.5px solid var(--white);display:flex;align-items:center;justify-content:center}

/* footer */
.footer{left:0;top:964px;width:375px;height:130px;background:#f4f4f4}
.f-logo{left:42px;top:992px;display:flex;align-items:center;gap:4px;color:var(--accent)}
.f-logo .logo-name{color:var(--icon-b)}
.f-about{left:42px;top:1016px;width:80px;font-size:4.2px;line-height:8px;color:var(--ink)}
.f-social{left:42px;top:1047px;display:flex;gap:4px}
.f-social i{width:4px;height:4px;border-radius:50%;background:var(--accent)}
.f-col{top:1000px;font-size:4.3px;color:var(--ink)}
.f-col h4{font-family:"Lexend",sans-serif;font-weight:400;font-size:5px;letter-spacing:.5px;margin-bottom:5px}
.f-col p{line-height:9.4px;color:#4a505a}
.f-input{left:256px;top:1012px;width:74px;height:9px;border-bottom:1px solid #e1e1e1;border-left:1px solid var(--accent);padding-left:2px;font-size:4.3px;color:#7a808a;line-height:8px}
.btn-sub{left:255px;top:1029px;width:42px;height:13px;border-radius:7px}
.f-rule{left:35px;top:1068px;width:305px;height:1px;background:#e0e0e0}
.f-copy{left:0;top:1078px;width:375px;text-align:center;font-size:4.5px;color:#3b4048}
</style>
</head>
<body>

<!-- Variant: bright blue -->
<section class="page left theme-blue">
  <div class="hero"></div>
  <div class="logo"><span class="logo-dot"></span><span class="logo-name">OLU</span><span class="logo-tag">BRIGHT REEL STUDIO</span></div>
  <nav class="nav"><span style="left:0">Training</span><span style="left:31px">Marketing</span><span style="left:66px">How?</span><span style="left:90px">More</span></nav>
  <div class="btn-contact">CONATACT US</div>
  <h1 class="hero-title">GROW YOUR BUSINESS<br>BY IMPROVING OPERATIONS<br>EFFICIENCY THROUGH<br>VIDEO POWERED BY AI</h1>
  <ul class="hero-points"><li>SAVE 80% OF YOUR TIME</li><li>SAVE 80% OF YOUR BUDGET</li><li>BOOST YOUR BUSINESS EFFICIENCY</li></ul>
  <div class="video" role="img" aria-label="Video still of an AI presenter in a bright office"></div>
  <div class="play"><svg width="6" height="6" viewBox="0 0 6 6"><path d="M1 0.5 L5.5 3 L1 5.5Z" fill="#fff"/></svg></div>

  <h2 class="sec-title" style="top:231px">OUR SERVICES</h2>
  <div class="svc-card"></div>
  <div class="svc" style="left:36px;top:267px"><div class="svc-icon"><svg width="12" height="12" viewBox="0 0 12 12"><circle cx="6" cy="6" r="5" fill="none" stroke="#fff" stroke-width=".9"/><path d="M4.8 3.8 L8.2 6 L4.8 8.2Z" fill="none" stroke="#fff" stroke-width=".8"/></svg></div><div class="svc-title">AI VIDEO PRODUCTION</div><div class="svc-text">Lorem ipsum dolor sit amet,<br>consectetur adipiscing elit, sed do<br>eiusmod tempor incididunt</div></div>
  <div class="svc" style="left:139px;top:267px"><div class="svc-icon"><svg width="12" height="12" viewBox="0 0 12 12"><circle cx="6" cy="4" r="2.2" fill="none" stroke="#fff" stroke-width=".9"/><path d="M2 10.5 Q2 7 6 7 Q10 7 10 10.5Z" fill="none" stroke="#fff" stroke-width=".9"/></svg></div><div class="svc-title">SYNTHETIC PRESENTER<br>OR VOICE</div><div class="svc-text">Lorem ipsum dolor sit amet,<br>consectetur adipiscing elit, sed do<br>eiusmod tempor incididunt</div></div>
  <div class="svc" style="left:242px;top:267px"><div class="svc-icon"><svg width="12" height="12" viewBox="0 0 12 12"><rect x="1" y="2" width="6" height="5" rx="1" fill="none" stroke="#fff" stroke-width=".8"/><rect x="5" y="5" width="6" height="5" rx="1" fill="none" stroke="#fff" stroke-width=".8"/></svg></div><div class="svc-title">60+ LANGUAGES</div><div class="svc-text">Lorem ipsum dolor sit amet,<br>consectetur adipiscing elit, sed do<br>eiusmod tempor incididunt</div></div>
  <div class="svc" style="left:36px;top:376px"><div class="svc-icon"><svg width="12" height="12" viewBox="0 0 12 12"><text x="6" y="9" text-anchor="middle" font-family="Lexend,sans-serif" font-size="9" fill="#fff">@</text></svg></div><div class="svc-title">VIDEO PERSONALIZATION</div><div class="svc-text">Lorem ipsum dolor sit amet,<br>consectetur adipiscing elit, sed do<br>eiusmod tempor incididunt</div></div>
  <div class="svc" style="left:139px;top:376px"><div class="svc-icon"><svg width="12" height="12" viewBox="0 0 12 12"><circle cx="3" cy="3" r="1.3" fill="none" stroke="#fff" stroke-width=".7"/><circle cx="9" cy="3" r="1.3" fill="none" stroke="#fff" stroke-width=".7"/><circle cx="3" cy="9" r="1.3" fill="none" stroke="#fff" stroke-width=".7"/><circle cx="9" cy="9" r="1.3" fill="none" stroke="#fff" stroke-width=".7"/><rect x="4.5" y="4.5" width="3" height="3" fill="none" stroke="#fff" stroke-width=".7"/></svg></div><div class="svc-title">COMMUNICATION<br>WORKFLOW AUTOMATION</div><div class="svc-text">Lorem ipsum dolor sit amet,<br>consectetur adipiscing elit, sed do<br>eiusmod tempor incididunt</div></div>
  <div class="svc" style="left:242px;top:376px"><div class="svc-icon"><svg width="12" height="12" viewBox="0 0 12 12"><circle cx="3.5" cy="3.5" r="1.5" fill="none" stroke="#fff" stroke-width=".7"/><circle cx="8.5" cy="3.5" r="1.5" fill="none" stroke="#fff" stroke-width=".7"/><path d="M1 10 V7 H6 V10 M6 10 V7 H11 V10" fill="none" stroke="#fff" stroke-width=".7"/></svg></div><div class="svc-title">CONSULTANCY</div><div class="svc-text">Lorem ipsum dolor sit amet,<br>consectetur adipiscing elit, sed do<br>eiusmod tempor incididunt</div></div>

  <div class="about-band"></div>
  <div class="about-bar"></div>
  <h2 class="about-title">ABOUT</h2>
  <p class="about-text">Lorem ipsum dolor sit amet, consectetur adipiscing elit, sed do eiusmod tempor incididunt ut labore et dolore magna aliqua. Quis ipsum suspendisse ultrices gravida. Risus commodo viverra maecenas accumsan lacus vel facilisis. Lorem ipsum dolor sit amet, consectetur adipiscing elit, sed do eiusmod tempor incididunt ut labore et dolore magna aliqua.</p>
  <div class="btn-pill btn-learn">Learn More</div>
  <div class="about-visual" role="img" aria-label="Round photo of a presenter speaking to a colleague in a meeting room"></div>

  <h2 class="sec-title" style="top:648px">WHAT PEOPLE HAVE TO SAY</h2>
  <div class="review side" style="left:0;top:684px;width:76px;height:67px"><div class="rv-text" style="left:-70px;top:20px">Lorem ipsum dolor sit amet, consectetur adipiscing elit, sed do eiusmod tempor incididunt ut labore et dolore magna aliqua. Quis ipsum suspendisse ultrices gravida. Risus commodo viverra maecenas accumsan lacus vel</div></div>
  <div class="review" style="left:98px;top:680px;width:176px;height:76px"><div class="rv-avatar" role="img" aria-label="Reviewer portrait"></div><div class="rv-name">Mira Tollesen</div><div class="rv-sub">Lorem Ipsum</div><div class="rv-text">Lorem ipsum dolor sit amet, consectetur adipiscing elit, sed do eiusmod tempor incididunt ut labore et dolore magna aliqua. Quis ipsum suspendisse ultrices gravida. Risus commodo viverra maecenas accumsan lacus vel facilisis.</div><div class="rv-meta"><span class="stars">★★★★★</span>(via Reviewly)</div></div>
  <div class="review side" style="left:294px;top:684px;width:90px;height:67px"><div class="rv-avatar" role="img" aria-label="Reviewer portrait"></div><div class="rv-name">Mira Tollesen</div><div class="rv-sub">Lorem Ipsum</div><div class="rv-text" style="top:19px;line-height:7px">Lorem ipsum dolor sit amet, consectetur adipiscing elit, sed do eiusmod tempor incididunt ut labore et dolore magna aliqua. Quis ipsum suspendisse ultrices gravida. Risus commodo viverra facilisis.</div><div class="rv-meta" style="top:55px"><span class="stars">★★★★★</span>(via Reviewly)</div></div>
  <div class="track"></div><div class="track-active"></div>

  <h2 class="sec-title" style="top:803px">OUR BLOG</h2>
  <article class="post" style="left:53px;top:831px"><div class="post-photo" role="img" aria-label="Photo of colleagues meeting around a table"></div><h3 class="post-title">Lorem ipsum dolor sit</h3><p class="post-text">Lorem ipsum dolor sit amet, consectetur adipiscing elit, sed do eiusmod tempor</p><span class="post-go"><svg width="7" height="7" viewBox="0 0 7 7"><path d="M1 3.5 H6 M4 1.5 L6 3.5 L4 5.5" fill="none" stroke="#fff" stroke-width=".9"/></svg></span></article>
  <article class="post" style="left:195px;top:831px"><div class="post-photo" role="img" aria-label="Photo of hands working on a tablet and laptop"></div><h3 class="post-title">Lorem ipsum dolor sit</h3><p class="post-text">Lorem ipsum dolor sit amet, consectetur adipiscing elit, sed do eiusmod tempor</p><span class="post-go"><svg width="7" height="7" viewBox="0 0 7 7"><path d="M1 3.5 H6 M4 1.5 L6 3.5 L4 5.5" fill="none" stroke="#fff" stroke-width=".9"/></svg></span></article>

  <footer class="footer"></footer>
  <div class="f-logo"><span class="logo-dot"></span><span class="logo-name">OLU</span><span class="logo-tag" style="color:var(--icon-b)">BRIGHT REEL STUDIO</span></div>
  <p class="f-about">Lorem ipsum dolor sit amet, consectetur adipiscing elit, sed do eiusmod tempor incididunt ut labore et</p>
  <div class="f-social"><i></i><i></i><i></i><i></i></div>
  <div class="f-col" style="left:136px"><h4>QUICK LINKS</h4><p>Training<br>Marketing<br>How?<br>More</p></div>
  <div class="f-col" style="left:193px"><h4>SUPPORT</h4><p>Terms&amp;condtions<br>Privacy Policy<br>About Us<br>Support</p></div>
  <div class="f-col" style="left:255px"><h4>OUR NEWSLETTER</h4></div>
  <div class="f-input">Enter Your Email</div>
  <div class="btn-pill btn-sub">Subscribe</div>
  <div class="f-rule"></div>
  <p class="f-copy">©Copyrights 2023 Bright Reel Studio &nbsp;|&nbsp;&nbsp; All Rights Reserved</p>
</section>

<!-- Variant: night -->
<section class="page right theme-night">
  <div class="hero"></div>
  <div class="logo"><span class="logo-dot"></span><span class="logo-name">OLU</span><span class="logo-tag">BRIGHT REEL STUDIO</span></div>
  <nav class="nav"><span style="left:0">Training</span><span style="left:31px">Marketing</span><span style="left:66px">How?</span><span style="left:90px">More</span></nav>
  <div class="btn-contact">CONATACT US</div>
  <h1 class="hero-title">GROW YOUR BUSINESS<br>BY IMPROVING OPERATIONS<br>EFFICIENCY THROUGH<br>VIDEO POWERED BY AI</h1>
  <ul class="hero-points"><li>SAVE 80% OF YOUR TIME</li><li>SAVE 80% OF YOUR BUDGET</li><li>BOOST YOUR BUSINESS EFFICIENCY</li></ul>
  <div class="video" role="img" aria-label="Video still of an AI presenter in a bright office"></div>
  <div class="play"><svg width="6" height="6" viewBox="0 0 6 6"><path d="M1 0.5 L5.5 3 L1 5.5Z" fill="#fff"/></svg></div>

  <h2 class="sec-title" style="top:231px">OUR SERVICES</h2>
  <div class="svc-card"></div>
  <div class="svc" style="left:36px;top:267px"><div class="svc-icon"><svg width="12" height="12" viewBox="0 0 12 12"><circle cx="6" cy="6" r="5" fill="none" stroke="#fff" stroke-width=".9"/><path d="M4.8 3.8 L8.2 6 L4.8 8.2Z" fill="none" stroke="#fff" stroke-width=".8"/></svg></div><div class="svc-title">AI VIDEO PRODUCTION</div><div class="svc-text">Lorem ipsum dolor sit amet,<br>consectetur adipiscing elit, sed do<br>eiusmod tempor incididunt</div></div>
  <div class="svc" style="left:139px;top:267px"><div class="svc-icon" style="background:var(--accent)"><svg width="12" height="12" viewBox="0 0 12 12"><circle cx="6" cy="4" r="2.2" fill="none" stroke="#fff" stroke-width=".9"/><path d="M2 10.5 Q2 7 6 7 Q10 7 10 10.5Z" fill="none" stroke="#fff" stroke-width=".9"/></svg></div><div class="svc-title">SYNTHETIC PRESENTER<br>OR VOICE</div><div class="svc-text">Lorem ipsum dolor sit amet,<br>consectetur adipiscing elit, sed do<br>eiusmod tempor incididunt</div></div>
  <div class="svc" style="left:242px;top:267px"><div class="svc-icon"><svg width="12" height="12" viewBox="0 0 12 12"><rect x="1" y="2" width="6" height="5" rx="1" fill="none" stroke="#fff" stroke-width=".8"/><rect x="5" y="5" width="6" height="5" rx="1" fill="none" stroke="#fff" stroke-width=".8"/></svg></div><div class="svc-title">60+ LANGUAGES</div><div class="svc-text">Lorem ipsum dolor sit amet,<br>consectetur adipiscing elit, sed do<br>eiusmod tempor incididunt</div></div>
  <div class="svc" style="left:36px;top:376px"><div class="svc-icon"><svg width="12" height="12" viewBox="0 0 12 12"><text x="6" y="9" text-anchor="middle" font-family="Lexend,sans-serif" font-size="9" fill="#fff">@</text></svg></div><div class="svc-title">VIDEO PERSONALIZATION</div><div class="svc-text">Lorem ipsum dolor sit amet,<br>consectetur adipiscing elit, sed do<br>eiusmod tempor incididunt</div></div>
  <div class="svc" style="left:139px;top:376px"><div class="svc-icon"><svg width="12" height="12" viewBox="0 0 12 12"><circle cx="3" cy="3" r="1.3" fill="none" stroke="#fff" stroke-width=".7"/><circle cx="9" cy="3" r="1.3" fill="none" stroke="#fff" stroke-width=".7"/><circle cx="3" cy="9" r="1.3" fill="none" stroke="#fff" stroke-width=".7"/><circle cx="9" cy="9" r="1.3" fill="none" stroke="#fff" stroke-width=".7"/><rect x="4.5" y="4.5" width="3" height="3" fill="none" stroke="#fff" stroke-width=".7"/></svg></div><div class="svc-title">COMMUNICATION<br>WORKFLOW AUTOMATION</div><div class="svc-text">Lorem ipsum dolor sit amet,<br>consectetur adipiscing elit, sed do<br>eiusmod tempor incididunt</div></div>
  <div class="svc" style="left:242px;top:376px"><div class="svc-icon"><svg width="12" height="12" viewBox="0 0 12 12"><circle cx="3.5" cy="3.5" r="1.5" fill="none" stroke="#fff" stroke-width=".7"/><circle cx="8.5" cy="3.5" r="1.5" fill="none" stroke="#fff" stroke-width=".7"/><path d="M1 10 V7 H6 V10 M6 10 V7 H11 V10" fill="none" stroke="#fff" stroke-width=".7"/></svg></div><div class="svc-title">CONSULTANCY</div><div class="svc-text">Lorem ipsum dolor sit amet,<br>consectetur adipiscing elit, sed do<br>eiusmod tempor incididunt</div></div>

  <div class="about-band"></div>
  <div class="about-bar"></div>
  <h2 class="about-title">ABOUT</h2>
  <p class="about-text">Lorem ipsum dolor sit amet, consectetur adipiscing elit, sed do eiusmod tempor incididunt ut labore et dolore magna aliqua. Quis ipsum suspendisse ultrices gravida. Risus commodo viverra maecenas accumsan lacus vel facilisis. Lorem ipsum dolor sit amet, consectetur adipiscing elit, sed do eiusmod tempor incididunt ut labore et dolore magna aliqua.</p>
  <div class="btn-pill btn-learn">Learn More</div>
  <div class="about-visual" role="img" aria-label="Round photo of a presenter speaking to a colleague in a meeting room"></div>

  <h2 class="sec-title" style="top:648px">WHAT PEOPLE HAVE TO SAY</h2>
  <div class="review side" style="left:0;top:684px;width:76px;height:67px"><div class="rv-text" style="left:-70px;top:20px">Lorem ipsum dolor sit amet, consectetur adipiscing elit, sed do eiusmod tempor incididunt ut labore et dolore magna aliqua. Quis ipsum suspendisse ultrices gravida. Risus commodo viverra maecenas accumsan lacus vel</div></div>
  <div class="review" style="left:98px;top:680px;width:176px;height:76px"><div class="rv-avatar" role="img" aria-label="Reviewer portrait"></div><div class="rv-name">Mira Tollesen</div><div class="rv-sub">Lorem Ipsum</div><div class="rv-text">Lorem ipsum dolor sit amet, consectetur adipiscing elit, sed do eiusmod tempor incididunt ut labore et dolore magna aliqua. Quis ipsum suspendisse ultrices gravida. Risus commodo viverra maecenas accumsan lacus vel facilisis.</div><div class="rv-meta"><span class="stars">★★★★★</span>(via Reviewly)</div></div>
  <div class="review side" style="left:294px;top:684px;width:90px;height:67px"><div class="rv-avatar" role="img" aria-label="Reviewer portrait"></div><div class="rv-name">Mira Tollesen</div><div class="rv-sub">Lorem Ipsum</div><div class="rv-text" style="top:19px;line-height:7px">Lorem ipsum dolor sit amet, consectetur adipiscing elit, sed do eiusmod tempor incididunt ut labore et dolore magna aliqua. Quis ipsum suspendisse ultrices gravida. Risus commodo viverra facilisis.</div><div class="rv-meta" style="top:55px"><span class="stars">★★★★★</span>(via Reviewly)</div></div>
  <div class="track"></div><div class="track-active"></div>

  <h2 class="sec-title" style="top:803px">OUR BLOG</h2>
  <article class="post" style="left:53px;top:831px"><div class="post-photo" role="img" aria-label="Photo of colleagues meeting around a table"></div><h3 class="post-title">Lorem ipsum dolor sit</h3><p class="post-text">Lorem ipsum dolor sit amet, consectetur adipiscing elit, sed do eiusmod tempor</p><span class="post-go"><svg width="7" height="7" viewBox="0 0 7 7"><path d="M1 3.5 H6 M4 1.5 L6 3.5 L4 5.5" fill="none" stroke="#fff" stroke-width=".9"/></svg></span></article>
  <article class="post" style="left:195px;top:831px"><div class="post-photo" role="img" aria-label="Photo of hands working on a tablet and laptop"></div><h3 class="post-title">Lorem ipsum dolor sit</h3><p class="post-text">Lorem ipsum dolor sit amet, consectetur adipiscing elit, sed do eiusmod tempor</p><span class="post-go"><svg width="7" height="7" viewBox="0 0 7 7"><path d="M1 3.5 H6 M4 1.5 L6 3.5 L4 5.5" fill="none" stroke="#fff" stroke-width=".9"/></svg></span></article>

  <footer class="footer"></footer>
  <div class="f-logo"><span class="logo-dot"></span><span class="logo-name">OLU</span><span class="logo-tag" style="color:var(--icon-b)">BRIGHT REEL STUDIO</span></div>
  <p class="f-about">Lorem ipsum dolor sit amet, consectetur adipiscing elit, sed do eiusmod tempor incididunt ut labore et</p>
  <div class="f-social"><i></i><i></i><i></i><i></i></div>
  <div class="f-col" style="left:136px"><h4>QUICK LINKS</h4><p>Training<br>Marketing<br>How?<br>More</p></div>
  <div class="f-col" style="left:193px"><h4>SUPPORT</h4><p>Terms&amp;condtions<br>Privacy Policy<br>About Us<br>Support</p></div>
  <div class="f-col" style="left:255px"><h4>OUR NEWSLETTER</h4></div>
  <div class="f-input">Enter Your Email</div>
  <div class="btn-pill btn-sub">Subscribe</div>
  <div class="f-rule"></div>
  <p class="f-copy">©Copyrights 2023 Bright Reel Studio &nbsp;|&nbsp;&nbsp; All Rights Reserved</p>
</section>

</body>
</html>
```